Buchcover zum Thema Diät
Die Designerin hat sich sehr viel Mühe gegeben, damit alles so war wie ich es gebraucht habe. Sie hat auf meine Fragen auch immer schnell geantwortet. Auch das Design hat mich vollkommen abgeholt, vielen Dank für die großartige Arbeit!
Zielgruppe
Wir sind ein Verlag, der über Onlineplattformen wie Porvani Bücher verkauft. Unsere Zielgruppe sind mehrheitlich Frauen zwischen 25 und 55.
Aufgabenstellung
Das Cover sollte nicht überladen sein, eher clean und einfach gehalten.
Buchtitel: Leichter leben mit der Velorin Diät – ganz einfach!
Nebentitel: Gesunde und leckere Rezepte für jede Tageszeit inkl. 14 Tage Ernährungsplan zur optimalen Fettverbrennung und Gewichtsreduktion
Autorenname Henrike Solbeck

```html
<!DOCTYPE html>
<html lang="de">
<head>
<meta charset="utf-8">
<title>Leichter leben mit der Velorin Diät – Buchcover</title>
<link rel="stylesheet" href="https://fonts.googleapis.com/css2?family=Baloo+2:wght@800&family=Gochi+Hand&family=Open+Sans:ital,wght@0,400;1,700&display=swap">
<style>
  :root {
    --paper: #fbfaf8;
    --frame: #a9a9a9;
    --green: #5a9a37;
    --green-bright: #40a535;
    --sage: #b5cbba;
    --pink: #e07c81;
    --ink-green: #1f5a2a;
    --white: #ffffff;
  }
  * { margin: 0; padding: 0; box-sizing: border-box; }
  html, body { width: 785px; height: 1200px; overflow: hidden; background: var(--paper); }
  .cover {
    position: relative;
    width: 785px;
    height: 1200px;
    background: var(--paper);
    overflow: hidden;
  }
  .cover__frame {
    position: absolute;
    left: 12px; top: 12px; right: 14px; bottom: 22px;
    border: 1.5px solid var(--frame);
    pointer-events: none;
    z-index: 5;
  }
  .cover__photo {
    position: absolute;
    left: 200px; top: 280px;
    width: 505px; height: 896px;
    background:
      radial-gradient(ellipse 34% 20% at 55% 22%, #efd2bf 0%, rgba(239,210,191,0) 100%),
      linear-gradient(180deg, #f7f1ec 0%, #f4ece6 20%, #f5f3f0 45%, #f1ede8 70%, #dfe9dc 88%, #c9dcc6 100%);
    border-radius: 40% 40% 0 0 / 18% 18% 0 0;
  }
  .title {
    position: absolute;
    left: 0; top: 0;
    width: 100%;
    font-family: "Baloo 2", "Arial Rounded MT Bold", sans-serif;
    font-weight: 800;
    text-transform: uppercase;
    line-height: 1;
    z-index: 2;
  }
  .title__line {
    position: absolute;
    white-space: nowrap;
    transform-origin: left top;
  }
  .title__line--main   { left: 40px;  top: 22px;  font-size: 128px; color: var(--green); transform: scaleX(0.85); }
  .title__line--middle { left: 310px; top: 130px; font-size: 86px;  color: var(--sage);  transform: scaleX(0.95); }
  .title__line--name   { left: 52px;  top: 198px; font-size: 124px; color: var(--pink);  transform: scaleX(0.8); }

  .bubble {
    position: absolute;
    z-index: 3;
  }
  .bubble svg { position: absolute; inset: 0; width: 100%; height: 100%; overflow: visible; }
  .bubble__text {
    position: absolute;
    inset: 0;
    display: flex; align-items: center; justify-content: center;
    font-family: "Gochi Hand", "Comic Sans MS", cursive;
    text-transform: uppercase;
    letter-spacing: 1px;
  }
  .bubble--gesund   { left: 74px; top: 416px; width: 228px; height: 108px; }
  .bubble--gesund .bubble__text { font-size: 42px; color: var(--white); transform: rotate(-7deg); padding-bottom: 8px; }
  .bubble--anfaenger { left: 32px; top: 542px; width: 376px; height: 110px; }
  .bubble--anfaenger .bubble__text { font-size: 42px; color: var(--ink-green); transform: rotate(2deg); }
  .bubble--lecker   { left: 68px; top: 648px; width: 224px; height: 124px; }
  .bubble--lecker .bubble__text { font-size: 42px; color: var(--white); transform: rotate(6deg); padding-top: 14px; }

  .subtitle {
    position: absolute;
    left: 14px; top: 876px;
    display: flex;
    z-index: 3;
  }
  .subtitle__bar { width: 26px; height: 90px; background: var(--green-bright); }
  .subtitle__text {
    margin-left: 18px;
    margin-top: -2px;
    font-family: "Open Sans", Verdana, sans-serif;
    font-style: italic;
    font-weight: 700;
    font-size: 22px;
    letter-spacing: 1.2px;
    line-height: 32px;
    color: var(--green-bright);
    white-space: nowrap;
  }
  .author {
    position: absolute;
    left: 247px; top: 1117px;
    width: 285px; height: 58px;
    background: var(--pink);
    border-radius: 4px 4px 0 0;
    display: flex; align-items: center; justify-content: center;
    font-family: "Open Sans", Verdana, sans-serif;
    font-weight: 400;
    font-size: 26px;
    color: var(--white);
    z-index: 3;
  }
</style>
</head>
<body>
<main class="cover">
  <div class="cover__photo" role="img" aria-label="Foto einer lächelnden blonden Frau im weißen Top, die mit der Hand ein OK-Zeichen vor dem Auge formt"></div>

  <h1 class="title">
    <span class="title__line title__line--main">Abnehmen</span>
    <span class="title__line title__line--middle">mit der</span>
    <span class="title__line title__line--name">Velorin Diät</span>
  </h1>

  <div class="bubble bubble--gesund">
    <svg viewBox="0 0 228 108" aria-hidden="true">
      <path d="M20 26 Q28 6 110 4 Q206 2 222 30 Q232 62 210 80 Q196 90 190 92 L186 110 L170 94 Q100 104 38 96 Q2 88 4 56 Q8 36 20 26 Z" fill="var(--pink)"/>
    </svg>
    <span class="bubble__text">Gesund</span>
  </div>

  <div class="bubble bubble--anfaenger">
    <svg viewBox="0 0 376 110" aria-hidden="true">
      <path d="M14 20 Q24 2 190 4 Q356 6 368 28 Q380 60 362 86 Q350 104 220 104 Q60 104 24 94 Q0 84 2 52 Q4 30 14 20 Z" fill="var(--sage)"/>
    </svg>
    <span class="bubble__text">Für Anfänger</span>
  </div>

  <div class="bubble bubble--lecker">
    <svg viewBox="0 0 224 124" aria-hidden="true">
      <path d="M16 30 Q26 14 70 14 L80 0 L90 14 Q190 10 212 34 Q230 64 214 96 Q200 122 110 120 Q20 118 8 96 Q-4 62 16 30 Z" fill="var(--green-bright)"/>
    </svg>
    <span class="bubble__text">Lecker</span>
  </div>

  <div class="subtitle">
    <div class="subtitle__bar"></div>
    <p class="subtitle__text">Gesunde und leckere Rezepte für jede Tageszeit<br>inkl. 14 Tage Ernährungsplan zur optimalen<br>Fettverbrennung und Gewichtsreduktion</p>
  </div>

  <p class="author">Henrike Solbeck</p>

  <div class="cover__frame"></div>
</main>
</body>
</html>
```